"Dental Meadow" clinic needs brochure

a creative design is needed for flyer for a dental clinic, all info available on this website www.dentalmeadow-sample.ae, new imagery needed.

Industry/Entity Type

Clinic

```html
<!DOCTYPE html>
<html lang="en">
<head>
<meta charset="utf-8">
<title>Dental Meadow Clinic – Brochure</title>
<link href="https://fonts.googleapis.com/css2?family=Source+Sans+3:ital,wght@0,400;0,600;0,700;1,700&display=swap" rel="stylesheet">
<style>
:root{
  --blue:#1f4ff0;
  --white:#ffffff;
  --ink:#1c1c1c;
  --strip:rgba(236,236,236,.88);
}
*{box-sizing:border-box;margin:0;padding:0}
html,body{width:1200px;height:1200px;overflow:hidden;background:var(--white)}
body{font-family:"Source Sans 3",Arial,sans-serif;color:var(--ink)}
.stage{position:absolute;left:0;top:0;width:1500px;height:1500px;transform:scale(.8);transform-origin:0 0}
.shapes{position:absolute;left:0;top:0}
.abs{position:absolute}
.brand{left:82px;top:238px;display:flex;align-items:center;gap:14px;color:var(--white);font-weight:600;font-size:27px;letter-spacing:1px;text-transform:uppercase}
.brand-dot{width:46px;height:46px;border:3px solid var(--white);border-radius:50%}
.copy{font-size:14.6px;line-height:20px;white-space:nowrap}
.about{left:43px;top:385px}
.section-title{font-weight:700;font-style:italic;color:var(--blue);font-size:21px;line-height:22px}
.about p{margin-bottom:20px}
.right-copy .line{position:absolute;white-space:nowrap}
.photo-label{position:absolute;font-size:19px;line-height:24px;color:var(--ink);transform:rotate(-45deg);transform-origin:0 0;white-space:nowrap}
.services-title{left:788px;top:804px;color:var(--white);font-size:21px;font-weight:700;font-style:italic}
.service{position:absolute;border:2px solid var(--white);color:var(--white);padding:4px 12px 6px 12px;background:var(--blue)}
.service h3{font-size:17.5px;font-weight:600;line-height:22px}
.service li{list-style:none;font-size:14.6px;line-height:20px;white-space:nowrap}
.service li::before{content:"• "}
.general{left:785px;top:838px;width:205px;height:154px}
.pediatric{left:1009px;top:836px;width:272px;height:132px;padding-left:16px}
.biological{left:1129px;top:978px;width:311px;height:101px;padding-left:17px}
.cosmetic{left:912px;top:1003px;width:210px;height:115px;padding-left:17px}
.prosthetic{left:1129px;top:1086px;width:233px;height:119px}
.emergency{left:1129px;top:1214px;width:233px;height:34px}
</style>
</head>
<body>
<div class="stage">
  <svg class="shapes" width="1500" height="1500" viewBox="0 0 1500 1500">
    <defs>
      <linearGradient id="gDenture" x1="0" y1="0" x2="1" y2="1"><stop offset="0" stop-color="#e4d6b8"/><stop offset="1" stop-color="#b9aa8c"/></linearGradient>
      <linearGradient id="gSmile" x1="0" y1="0" x2="1" y2="1"><stop offset="0" stop-color="#f2ecea"/><stop offset="1" stop-color="#e07d9a"/></linearGradient>
      <linearGradient id="gInlay" x1="0" y1="0" x2="1" y2="1"><stop offset="0" stop-color="#c8cbcf"/><stop offset="1" stop-color="#e2d1b2"/></linearGradient>
      <linearGradient id="gImplant" x1="0" y1="0" x2="1" y2="1"><stop offset="0" stop-color="#e9a3b4"/><stop offset="1" stop-color="#c9cdd3"/></linearGradient>
    </defs>
    <polygon fill="var(--blue)" points="5,220 735,220 1480,965 1480,1265 1045,1265 620,833"/>
    <polygon role="img" aria-label="Photo of a chrome cobalt partial denture" fill="url(#gDenture)" points="445,297 628,480 445,663 262,480"/>
    <polygon role="img" aria-label="Photo of a bright smile with porcelain veneers" fill="url(#gSmile)" points="620,475 800,655 620,835 440,655"/>
    <polygon role="img" aria-label="Photo of ceramic inlay and onlay restorations" fill="url(#gInlay)" points="800,293 978,471 800,649 622,471"/>
    <polygon role="img" aria-label="Photo of a single dental implant between teeth" fill="url(#gImplant)" points="985,480 1165,660 985,840 805,660"/>
    <line x1="620" y1="475" x2="620" y2="833" stroke="var(--white)" stroke-width="6"/>
    <polygon fill="var(--strip)" points="262,480 445,297 462,314 279,497"/>
    <polygon fill="var(--strip)" points="440,655 617,478 617,512 457,672"/>
    <polygon fill="var(--strip)" points="622,471 800,293 817,310 639,488"/>
    <polygon fill="var(--strip)" points="805,660 985,480 1002,497 822,677"/>
  </svg>

  <div class="abs brand"><span class="brand-dot"></span>Dental Meadow</div>

  <div class="photo-label" style="left:268px;top:474px">Chrome Cobalt Partial Denture</div>
  <div class="photo-label" style="left:474px;top:621px">Porcelain Veneers</div>
  <div class="photo-label" style="left:660px;top:433px">Inlay and Onlay</div>
  <div class="photo-label" style="left:828px;top:637px">Single Dental Implant</div>

  <div class="abs about copy">
    <h2 class="section-title">ABOUT US</h2>
    <p>Our Practice:<br>We are a dental<br>practice devoted to<br>restoring and enhancing<br>the natural beauty of your<br>smile using conservative,<br>state-of-the-art procedures that will<br>result in beautiful, long lasting smiles.</p>
    <p>High Standards:<br>A standard of excellence in personalized dental<br>care enables us to provide the quality dental<br>services our patients deserve.&nbsp; We provide compre-<br>hensive treatment planning and use restorative and<br>cosmetic dentistry to achieve your optimal dental health.<br>Should a dental emergency occur, we make every effort to see<br>and care for you immediately.</p>
    <p>Education &amp; Prevention:<br>As a practice, we are true believers that preventive care and education are the<br>keys to optimal dental health.&nbsp; We strive to provide “dental health care” vs.<br>“disease care.”&nbsp; That’s why we focus on thorough exams – checking the overall health<br>of your teeth and gums, performing oral cancer exams, and taking x-rays when neces-<br>sary.&nbsp; We also know that routine cleanings, flossing, sealants, and fluoride are all helpful in<br>preventing dental disease.&nbsp; Not only are we focused on the beauty of your smile, we’re also<br>concerned about your health.&nbsp; A review of your medical history can help us stay informed of your<br>overall health, any new medications, and any illnesses that may impact your dental health.</p>
    <p>Uncompromising Safety:<br>Infection control in our office is also very important to us.&nbsp; To protect our patients and ourselves,<br>we strictly maintain sterilization and cross contamination processes using standards recommend-<br>ed by the Regional Health Authority (RHA), Health Ministry (HM).</p>
    <p>Training &amp; Expertise:<br>As your dental health professionals, we want you to be confident knowing that we are a team of<br>highly trained and skilled clinicians.&nbsp; We pride ourselves in providing the care you need to keep your<br>smile healthy.&nbsp; To give you the best possible service and results, we are committed to continual<br>education and learning.&nbsp; We attend dental lectures, meetings, and dental conventions to stay<br>informed of new techniques, the latest products, and the newest equipment that a modern dental<br>office can utilize to provide state-of-the-art dental care.&nbsp; Also, being members of various professional<br>dental associations helps us to stay abreast of the changes and recommendations for our profession.</p>
  </div>

  <div class="right-copy copy">
    <span class="line" style="left:832px;top:285px">A Positive Experience:</span>
    <span class="line" style="left:852px;top:305px">Building a foundation of trust by treating our patients as special individuals is vital to</span>
    <span class="line" style="left:872px;top:325px">our success.  We understand how uneasy some patients may feel about their dental</span>
    <span class="line" style="left:892px;top:345px">visits, and how we can make a difference in providing a relaxing and positive</span>
    <span class="line" style="left:912px;top:365px">experience.  Our entire team is dedicated to providing you with excellent,</span>
    <span class="line" style="left:932px;top:385px">personalized care and service to make your visits as comfortable and</span>
    <span class="line" style="left:952px;top:405px">pleasant as possible.</span>
    <span class="line" style="left:972px;top:425px">We thank you for allowing us to take care of your dental needs and</span>
    <span class="line" style="left:992px;top:445px">look forward to serving you.</span>
    <span class="line" style="left:1012px;top:465px">Make an appointment today.....we’ll give you a reason to smile!</span>

    <span class="line" style="left:1052px;top:505px">Our Mission Dental Meadow Clinic</span>
    <span class="line" style="left:1072px;top:525px">Render excellent dental care to our patients and to</span>
    <span class="line" style="left:1092px;top:545px">help them appreciate its value in their lives.</span>
    <span class="line" style="left:1112px;top:565px">Provide in a family dentistry environment the</span>
    <span class="line" style="left:1132px;top:585px">maximum in quality oral health care, including</span>
    <span class="line" style="left:1152px;top:605px">diagnosis, treatment and maintenance in</span>
    <span class="line" style="left:1172px;top:625px">order to allow our patients the opportu-</span>
    <span class="line" style="left:1192px;top:645px">nity to retain their teeth for a</span>
    <span class="line" style="left:1212px;top:665px">lifetime.</span>
    <span class="line" style="left:1232px;top:685px">Create a supportive atmo-</span>
    <span class="line" style="left:1252px;top:705px">sphere which encourages</span>
    <span class="line" style="left:1272px;top:725px">personal growth and a</span>
    <span class="line" style="left:1292px;top:745px">harmonious relation-</span>
    <span class="line" style="left:1312px;top:765px">ship among</span>
    <span class="line" style="left:1332px;top:785px">doctors, staff</span>
    <span class="line" style="left:1352px;top:805px">and patients.</span>
  </div>

  <h2 class="abs services-title">OUR SERVICES</h2>

  <div class="service general"><h3>General Dentistry</h3><ul>
    <li>Scaling and Polishing</li><li>White fillings</li><li>Root canal Treatment</li><li>Extraction</li><li>Inlays and onlays</li><li>Surgical Removal of Teeth</li></ul></div>
  <div class="service pediatric"><h3>Pediatric Dentistry</h3><ul>
    <li>White fillings</li><li>Flouride treatment</li><li>Pulpotomy and pulpectomy</li><li>Extraction</li><li>Space maintainer and Zircon crowns</li></ul></div>
  <div class="service biological"><h3>Biological Dentistry</h3><ul>
    <li>Safe Removal of Amalgam Filling (SAFE)</li><li>Note: All our materials Bio-compatible<br>Materials</li></ul></div>
  <div class="service cosmetic"><h3>Cosmetic Dentistry</h3><ul>
    <li>Veneers (Hollywood smile)</li><li>Smile design</li><li>Lithix Crowns</li><li>Lumi Bleaching</li></ul></div>
  <div class="service prosthetic"><h3>Prosthetic Dentistry</h3><ul>
    <li>Crown and bridges</li><li>Fiber post</li><li>Implants</li><li>Complete and Partial dentures</li></ul></div>
  <div class="service emergency"><h3>Emergency Dentistry</h3></div>
</div>
</body>
</html>
```